依頼詳細
【背景】
弊社は平成17年の創業以来、パチンコ店の広告物を主に企画提案〜制作、折込などの代理店業を行ってきました。
しかし、パチンコ業界の規制強化などの理由から、パチンコ業界以外の業種の広告物やBtoBの販促企画•制作、また最近では農家のブランディングなどの仕事にシフトしてきています。
そのような状況の中、弊社の代表自らもMBAのビジネススクールに通いマーケティング等を学び直しており、今後は現状の制作メインの仕事だけではなく、さらに川上のマーケティングや広告戦略といった、もっとクライアントに入り込んだお手伝いが出来る力をつけていきたいと考えています。
その為には再度、組織の再構築、強みを活かせる組織づくりを行っていく必要があり、設立10年を前に第二創業といった心づもりで企業理念を変更しようと考えています。
また、企業理念はこの会社は何の為に存在しているのかを言語化したものであり、在職中のスタッフだけではなく、今後採用予定の方にも共感した上で働いていただきたいと考えています。

【仕様】
・A3縦で制作してください
・納品はイラレデータでお願いします
・イメージは実際の経営理念から想像してください
記載項目
企業理念

Creative Happy!
-社会のHappy!
-顧客のHappy!
-仲間のHappy!
-家族のHappy!
-自分のHappy!

会社ロゴ

【解説(ココは記載不要です)】
Creative Happy! … 広告物を作るのではなく、その先にあるHappyを作っているという意識。
例えば、ケーキ屋さんのDMを作る際、「ケーキ屋さんのDMをつくっている」という意識ではなく「家族で美味しそうにこのケーキを食べている姿」つまり「その先のHappy!」を意識・想像して作ることが出来れば、仕事の質に大きな差が生じると考えています。

-社会のHappy!
-顧客のHappy!
-仲間のHappy!
-家族のHappy!
-自分のHappy!
仕事をする上で「Happy!を考える順番」を意味しています。
希望イメージ
シンプル 複雑
単色 カラフル
暗い 明るい
日常 高級
遊び心 厳粛
未来的 伝統的
女性的 男性的
希望する色
納品ファイル
• イラストレーター形式 (.ai)
補足説明
■ 選んだ理由

まずイメージが明るくHAPPYな感じがしたこと
次に非常にわかりやすいビジュアルでストーリーを作ってくださったことが
kitazono-teさんのデザインを選んだ理由です。

■ 提案者全員のお礼・コメント

皆様にはご提案をいただき感謝いたします。
今回、大変多くの方からご提案をいただき、素敵なデザインが他にもあり社内でも選考するのに随分意見が出ました。

今回は弊社の社内的なポスターでしたが、弊社は広告代理業を行っているためチラシやDMなど他のグラフィックデザインも仕事として発生しています。(携帯電話のチラシなど)
またお願いすることもあるかと思いますので、どうぞよろしくお願いします。

```html
<!DOCTYPE html>
<html lang="ja">
<head>
<meta charset="UTF-8">
<title>Creative Happy! 企業理念ポスター</title>
<link rel="stylesheet" href="https://fonts.googleapis.com/css2?family=Noto+Sans+JP:wght@400;500&family=Poppins:wght@300;400&display=swap">
<style>
  :root {
    --family: #f4a11c;
    --team: #3f8fd9;
    --society: #ec5a34;
    --client: #5cb94b;
    --self: #f07c9d;
    --paper: #ffffff;
    --ink: #555555;
    --ink-soft: #666666;
    --accent: #f07c9d;
  }
  html, body {
    margin: 0;
    padding: 0;
    overflow: hidden;
    background: var(--paper);
  }
  .poster {
    position: relative;
    width: 846px;
    height: 1200px;
    overflow: hidden;
    background: var(--paper);
    font-family: "Noto Sans JP", sans-serif;
  }
  .stripe {
    position: absolute;
    top: 0;
    height: 900px;
    overflow: hidden;
  }
  .stripe--family  { left: 0;     width: 176px; background: var(--family); }
  .stripe--team    { left: 184px; width: 172px; background: var(--team); }
  .stripe--society { left: 364px; width: 172px; background: var(--society); }
  .stripe--client  { left: 544px; width: 172px; background: var(--client); }
  .stripe--self    { left: 724px; width: 122px; background: var(--self); }

  .glow {
    position: absolute;
    width: 34px;
    height: 34px;
    margin-left: -17px;
    border-radius: 50%;
    background: radial-gradient(circle, rgba(255,255,255,1) 0%, rgba(255,255,255,0.85) 18%, rgba(255,255,255,0.25) 45%, rgba(255,255,255,0) 70%);
  }
  .glow--small { width: 22px; height: 22px; margin-left: -11px; }

  .value {
    position: absolute;
    left: 50%;
    transform: translateX(-50%);
    writing-mode: vertical-rl;
    color: var(--paper);
    font-weight: 500;
    font-size: 60px;
    line-height: 1;
    letter-spacing: 0.04em;
    white-space: nowrap;
  }
  .value__suffix {
    font-size: 48px;
    letter-spacing: 0.1em;
  }

  .footer {
    position: absolute;
    left: 0;
    top: 900px;
    width: 846px;
    height: 300px;
    text-align: center;
  }
  .footer__lead {
    margin: 58px 0 0;
    font-size: 19px;
    letter-spacing: 0.28em;
    color: var(--ink-soft);
    font-weight: 400;
  }
  .footer__motto {
    margin: 14px 0 0;
    font-family: "Poppins", sans-serif;
    font-weight: 300;
    font-size: 96px;
    line-height: 1.05;
    letter-spacing: 0.02em;
    color: var(--ink);
  }
  .footer__motto-mark {
    color: var(--accent);
    font-weight: 400;
  }
  .footer__company {
    margin: 26px 0 0;
    font-size: 24px;
    font-weight: 500;
    letter-spacing: 0.12em;
    color: var(--ink);
  }
</style>
</head>
<body>
<main class="poster">
  <section class="stripe stripe--family">
    <span class="glow" style="left:50%;top:60px"></span>
    <span class="glow glow--small" style="left:50%;top:180px"></span>
    <span class="glow" style="left:50%;top:830px"></span>
    <p class="value" style="top:270px;margin:0">『家族』<span class="value__suffix">の幸せ</span></p>
  </section>
  <section class="stripe stripe--team">
    <span class="glow glow--small" style="left:50%;top:40px"></span>
    <span class="glow" style="left:50%;top:150px"></span>
    <span class="glow glow--small" style="left:50%;top:820px"></span>
    <p class="value" style="top:270px;margin:0">『仲間』<span class="value__suffix">の幸せ</span></p>
  </section>
  <section class="stripe stripe--society">
    <span class="glow" style="left:50%;top:30px"></span>
    <span class="glow glow--small" style="left:50%;top:110px"></span>
    <span class="glow" style="left:50%;top:740px"></span>
    <span class="glow glow--small" style="left:50%;top:850px"></span>
    <p class="value" style="top:175px;margin:0">『社会』<span class="value__suffix">の幸せ</span></p>
  </section>
  <section class="stripe stripe--client">
    <span class="glow glow--small" style="left:50%;top:20px"></span>
    <span class="glow" style="left:50%;top:650px"></span>
    <span class="glow glow--small" style="left:50%;top:760px"></span>
    <span class="glow" style="left:50%;top:850px"></span>
    <p class="value" style="top:95px;margin:0">『顧客』<span class="value__suffix">の幸せ</span></p>
  </section>
  <section class="stripe stripe--self">
    <span class="glow" style="left:50%;top:620px"></span>
    <span class="glow glow--small" style="left:50%;top:720px"></span>
    <span class="glow" style="left:50%;top:820px"></span>
    <p class="value" style="top:85px;margin:0">『自分』<span class="value__suffix">の幸せ</span></p>
  </section>

  <footer class="footer">
    <p class="footer__lead">これからも、今まで以上に制作に関わる全てにHappyを!</p>
    <h1 class="footer__motto">Creative Happy<span class="footer__motto-mark">!</span></h1>
    <p class="footer__company">御社名（ダミー）</p>
  </footer>
</main>
</body>
</html>
```